Korean Homemade food restaurant just like what your mom cooks at home

I need a black and white simple and modern design according to my logo.
My restaurant name is Noru Kan (meaning of home cooking).
I need to have 솔찬(Noru Kan) in Korean need to be included. Once again 솔찬.
I am not sure if I need to include my name and number and adress.

솔찬 Noru Kan 418 Marlow Ct. Brookfield, ID 83512 Grant Oh Owner Cell:208-555-0183 Store:208-555-0297

Target Market(s)

business owners, university students

Industry/Entity Type

Restaurant

Contact Information for Business Card

This is traditional Korean food restaurant that targets university students during lunch and Korean business travelers at dinner.

Font styles to use
Sans Serif

Requirements
Must have
• Must have my logo.

```html
<!DOCTYPE html>
<html lang="en">
<head>
<meta charset="utf-8">
<title>Noru Kan — Business Card</title>
<link rel="stylesheet" href="https://fonts.googleapis.com/css2?family=Questrial&family=Noto+Sans+KR:wght@400;700;900&display=swap">
<style>
  :root {
    --bg: #eef1f3;
    --blue-light: #3ea6c8;
    --blue-mid: #1f6f96;
    --blue-deep: #0f4a6c;
    --navy: #0a3d5c;
    --ink: #1d5a7a;
    --white: #ffffff;
    --font-latin: "Questrial", "Noto Sans KR", sans-serif;
    --font-korean: "Noto Sans KR", sans-serif;
  }
  * { box-sizing: border-box; margin: 0; padding: 0; }
  html, body { width: 1200px; height: 1000px; overflow: hidden; }
  body { background: var(--bg); position: relative; font-family: var(--font-latin); }

  .card {
    position: absolute;
    left: 180px;
    width: 840px;
    height: 460px;
    overflow: hidden;
    box-shadow: 0 12px 30px rgba(0,0,0,0.18);
  }
  .card--front { top: 30px; background: radial-gradient(ellipse at 62% 38%, var(--blue-light) 0%, var(--blue-mid) 45%, var(--blue-deep) 100%); }
  .card--back { top: 515px; background: var(--white); }

  .card__shapes { position: absolute; inset: 0; width: 100%; height: 100%; }

  .brand-korean {
    position: absolute;
    left: 80px;
    top: 110px;
    width: 220px;
    text-align: center;
    font-family: var(--font-korean);
    font-weight: 900;
    font-size: 78px;
    color: var(--white);
    line-height: 1;
  }
  .brand-korean__mark {
    display: block;
    width: 90px;
    height: 90px;
    margin: 0 auto 22px;
    border-radius: 50%;
    background: var(--white);
  }

  .contact {
    position: absolute;
    left: 440px;
    top: 92px;
    color: var(--ink);
    font-size: 21px;
    line-height: 31px;
    white-space: nowrap;
  }
  .contact__line:nth-child(2) { padding-left: 3px; }
  .contact__line:nth-child(3) { padding-left: 8px; }
  .contact__line:nth-child(4) { padding-left: 12px; }
  .contact__line:nth-child(5) { padding-left: 17px; }
  .contact__line:nth-child(6) { padding-left: 21px; }
  .contact__name .ko,
  .contact__name .strong { font-family: var(--font-korean); font-weight: 700; }

  .brand-latin {
    position: absolute;
    left: 210px;
    top: 90px;
    width: 630px;
    text-align: center;
    font-size: 70px;
    line-height: 1.1;
    color: var(--white);
    letter-spacing: 1px;
  }
  .brand-latin__mark {
    display: block;
    width: 64px;
    height: 64px;
    margin: 0 auto 18px;
    border-radius: 50%;
    background: var(--white);
  }
</style>
</head>
<body>

  <section class="card card--front" aria-label="Business card front">
    <svg class="card__shapes" viewBox="0 0 840 460" aria-hidden="true">
      <polygon points="420,72 840,62 840,300 460,312" fill="var(--white)"/>
      <polygon points="404,74 412,74 452,314 444,314" fill="var(--white)"/>
    </svg>
    <div class="brand-korean">
      <span class="brand-korean__mark"></span>
      솔찬
    </div>
    <div class="contact">
      <div class="contact__line contact__name"><span class="ko">솔찬</span> Noru <span class="strong">Kan</span></div>
      <div class="contact__line">Grant Oh Owner</div>
      <div class="contact__line">Cell:208-555-0183</div>
      <div class="contact__line">Store:208-555-0297</div>
      <div class="contact__line">418 Marlow Ct.</div>
      <div class="contact__line">Brookfield, ID 83512</div>
    </div>
  </section>

  <section class="card card--back" aria-label="Business card back">
    <svg class="card__shapes" viewBox="0 0 840 460" aria-hidden="true">
      <polygon points="250,0 840,0 840,300 190,300" fill="var(--navy)"/>
      <rect x="0" y="405" width="840" height="6" fill="var(--navy)"/>
      <rect x="0" y="420" width="840" height="40" fill="var(--navy)"/>
    </svg>
    <div class="brand-latin">
      <span class="brand-latin__mark"></span>
      Noru Kan
    </div>
  </section>

</body>
</html>
```